Roadward Lane Management Company Website

Modern website Wordpress design using all greyscale photos with a pop of red (such as road closure signs or detour cones) for strategic emphasis. (see brand guide for color codes)
The creative goal is to leverage high-contrast, desaturated imagery to create a clean, professional, and industrial feel. The selective use of red will draw immediate attention to critical elements—such as road hazards, safety equipment, or key messages to ensure the viewer's focus is directed with purpose.

Brand guide, homepage content and logo are attached. Create clean professional user experience to market services to industry professionals.

```html
<!DOCTYPE html>
<html lang="en">
<head>
<meta charset="utf-8">
<title>Roadward Lane Management Company</title>
<link href="https://fonts.googleapis.com/css2?family=Archivo:wght@400;600;700;800;900&family=Inter:wght@400;500&display=swap" rel="stylesheet">
<style>
:root{
  --red:#ed1c24;
  --ink:#111111;
  --white:#ffffff;
  --card:#5a5a5a;
  --footer:#595959;
  --muted:#444444;
}
*{box-sizing:border-box;margin:0;padding:0}
html,body{width:779px;height:1200px;overflow:hidden;background:var(--white)}
body{position:relative;font-family:"Inter",Arial,sans-serif;color:var(--ink)}

.site-header{position:absolute;left:0;top:0;width:779px;height:58px;background:var(--white)}
.brand{position:absolute;left:39px;top:18px;display:flex;align-items:center;gap:5px;font-family:"Archivo",Arial,sans-serif;font-weight:800;font-size:17px;color:var(--ink)}
.brand-mark{width:12px;height:12px;background:var(--red)}
.main-nav a{position:absolute;top:24px;font-size:8.5px;color:var(--ink);text-decoration:none;letter-spacing:.2px}
.main-nav a.active{color:var(--red)}
.nav-cta{position:absolute;left:650px;top:14px;width:90px;height:30px;background:var(--red);color:var(--white);font-family:"Archivo",Arial,sans-serif;font-weight:800;font-size:10.5px;display:flex;align-items:center;justify-content:center}

.hero{position:absolute;left:0;top:58px;width:779px;height:385px;overflow:hidden}
.hero-photo{position:absolute;inset:0;background:linear-gradient(100deg,#484848 0%,#5a5a5a 40%,#6c6c6c 70%,#7a6666 100%)}
.hero-title{position:absolute;left:40px;top:94px;font-family:"Archivo",Arial,sans-serif;font-weight:800;font-size:30px;line-height:36px;color:var(--white);letter-spacing:.6px}
.hero-cta{position:absolute;left:39px;top:245px;width:90px;height:30px;background:var(--red);color:var(--white);font-family:"Archivo",Arial,sans-serif;font-weight:800;font-size:10.5px;display:flex;align-items:center;justify-content:center}
.hazard-band{position:absolute;left:0;top:443px;width:779px;height:19px;background:var(--red);border-bottom:3px solid var(--ink)}

.services{position:absolute;left:39px;top:505px;width:701px}
.services h2{text-align:center;font-family:"Archivo",Arial,sans-serif;font-weight:900;font-size:22px;letter-spacing:.8px}
.services .tagline{text-align:center;font-size:8.3px;color:var(--muted);margin-top:8px;letter-spacing:.1px}
.service-grid{position:absolute;left:0;top:60px;display:grid;grid-template-columns:repeat(4,168px);column-gap:10px;row-gap:12px}
.service-card{width:168px;height:192px;background:var(--card);position:relative}
.service-card .photo{width:168px;height:135px;background:linear-gradient(165deg,#cfcfcf 0%,#9a9a9a 100%)}
.service-card .photo.dark{background:linear-gradient(165deg,#707070 0%,#3f3f3f 100%)}
.service-card .photo.warm{background:linear-gradient(165deg,#bdbdbd 0%,#9a8a80 100%)}
.service-card h3{position:absolute;left:11px;top:150px;font-family:"Archivo",Arial,sans-serif;font-weight:800;font-size:11.5px;line-height:14px;color:var(--white)}
.service-card.featured{background:#e14b55}
.service-card.featured .photo{height:192px;background:linear-gradient(165deg,#ec6a72 0%,#d94650 100%)}
.service-card.featured h3{top:121px}

.site-footer{position:absolute;left:0;top:1015px;width:779px;height:185px;background:var(--footer);color:var(--white)}
.footer-brand{position:absolute;left:39px;top:34px;display:flex;align-items:center;gap:5px;font-family:"Archivo",Arial,sans-serif;font-weight:800;font-size:15px}
.footer-about{position:absolute;left:40px;top:85px;font-size:8.3px;line-height:13.5px}
.footer-col h4{font-family:"Archivo",Arial,sans-serif;font-weight:700;font-size:11.5px}
.footer-services{position:absolute;left:277px;top:28px}
.rule{width:23px;height:3px;background:var(--red);margin-top:6px}
.footer-services ul{list-style:none;margin-top:14px}
.footer-services li{font-size:8.3px;height:17px;display:flex;align-items:center;gap:9px}
.footer-services li::before{content:"";width:5px;height:5px;background:var(--red)}
.footer-partners{position:absolute;left:514px;top:28px;width:226px}
.badges{position:relative;margin-top:16px;height:80px}
.badge{position:absolute;background:#7a7a7a}
.footer-bottom{position:absolute;left:39px;top:153px;width:701px;border-top:1px solid #777;text-align:center;font-size:7.5px;padding-top:10px;letter-spacing:.2px}
</style>
</head>
<body>
<header class="site-header">
  <div class="brand"><span class="brand-mark"></span>Roadward</div>
  <nav class="main-nav">
    <a class="active" style="left:351px">HOME</a>
    <a style="left:404px">ABOUT</a>
    <a style="left:464px">SERVICES</a>
    <a style="left:537px">RENTALS</a>
    <a style="left:605px">JOBS</a>
    <div class="nav-cta">CONTACT</div>
  </nav>
</header>

<section class="hero">
  <div class="hero-photo" role="img" aria-label="Greyscale photo of a flagger in a hard hat holding a red stop sign"></div>
  <h1 class="hero-title">TRAFFIC CONTROL<br>SOLUTIONS<br>ENGINEERED FOR<br>SAFETY.</h1>
  <div class="hero-cta">CONTACT</div>
</section>
<div class="hazard-band"></div>

<section class="services">
  <h2>SERVICES</h2>
  <p class="tagline">SAFETY ISN’T A PRIORITY, IT’S THE FOUNDATION OF EVERYTHING WE DO</p>
  <div class="service-grid">
    <article class="service-card"><div class="photo warm" role="img" aria-label="Red and white striped channelizer on a road shoulder"></div><h3>Flagging &amp; Lane<br>Closures</h3></article>
    <article class="service-card"><div class="photo warm" role="img" aria-label="Orange single lane ahead sign with flags"></div><h3 style="left:8px">Signage &amp; Barricades</h3></article>
    <article class="service-card"><div class="photo warm" role="img" aria-label="Orange arrow sign beside a line of drums on a road"></div><h3 style="left:13px">Temporary Traffic<br>Control Plans</h3></article>
    <article class="service-card"><div class="photo warm" role="img" aria-label="Orange lane ends warning sign by a sidewalk"></div><h3 style="left:9px">Crash Attenuators &amp; Truck<br>Mounted Attenuators</h3></article>
    <article class="service-card"><div class="photo dark" role="img" aria-label="Orange traffic cone on cobblestones"></div><h3>Heavy Highway Traffic<br>Control</h3></article>
    <article class="service-card"><div class="photo" role="img" aria-label="Striped barricades with an orange detour sign"></div><h3 style="left:12px">Roadway Detours &amp;<br>Lane Shifts</h3></article>
    <article class="service-card featured"><div class="photo" role="img" aria-label="Red-tinted photo of a delineator post in a work zone"></div><h3 style="left:12px">Work Zone Safety<br>Consulting for<br>Compliance with State<br>and Federal regulations</h3></article>
    <article class="service-card"><div class="photo warm" role="img" aria-label="Orange traffic barrel with a warning light"></div><h3 style="left:12px">Event Traffic &amp; Crowd<br>Control</h3></article>
  </div>
</section>

<footer class="site-footer">
  <div class="footer-brand"><span class="brand-mark"></span>Roadward</div>
  <p class="footer-about">Serving Texas Industry to Ensure Safety,<br>Compliance, and Efficient Traffic Flow.</p>
  <div class="footer-col footer-services">
    <h4>Services</h4>
    <div class="rule"></div>
    <ul>
      <li>Road construction, maintenance, &amp; Detours</li>
      <li>Municipal &amp; State projects</li>
      <li>Private Sector &amp; Commercial Contractors</li>
      <li>Oil, Gas, Wind, Solar, &amp; Manufacturing</li>
    </ul>
  </div>
  <div class="footer-col footer-partners">
    <h4>Efficient Traffic Flow</h4>
    <div class="badges">
      <div class="badge" style="left:2px;top:4px;width:40px;height:28px"></div>
      <div class="badge" style="left:58px;top:10px;width:98px;height:18px"></div>
      <div class="badge" style="left:172px;top:2px;width:48px;height:30px"></div>
      <div class="badge" style="left:0;top:48px;width:60px;height:26px"></div>
      <div class="badge" style="left:84px;top:44px;width:34px;height:34px;border-radius:50%"></div>
    </div>
  </div>
  <div class="footer-bottom">©2025 ROADWARD- All rights reserved.</div>
</footer>
</body>
</html>
```